Banner for Vet Hospital 5m x 1.2m - Heat Stroke

Meadowlark Pet Hospital needs a Heat Stroke Banner for Summer.
The banner will be 5000mm long and 1200mm tall.

Our region has been hot this year and this summer is going to be extremely hot.
I want to warn people about heat stroke.
I want you to create a heat stroke banner that conveys the symptoms of heat stroke.

Pictures are better than words.
There should be IMAGES and WORDS that can be seen from the road 30m away and maybe some smaller words for people to read as they walk past.

Here are some of the signs of Heat Stroke:
- Panting which increases as heatstroke progresses
- Drooling, salivating
- Agitation, restlessness
- Very red or pale gums
- Bright red tongue
- Increased heart rate
- Breathing distress
- Vomiting Diarrhea (possibly with blood)
- Signs of mental confusion, delirium
- Dizziness, staggering
- Lethargy, weakness
- Muscle tremors
- Seizures
- Collapsing and lying down
- Little to no urine production
- Coma

I have attached characters that we often use in our advertising. They are optional.
I have done a mock up of the design I imagine. You could refine this design or make your own....or both.

Target Market(s)

Women aged 20 to 50.

Industry/Entity Type

Veterinary

Font styles to use
Sans Serif

Colors
fbed22
f78f20
ec1f27
ffffff

Requirements
Must have
• Heat Stroke Symtpms.
• Heat Stroke Warning.
• Summer theme.
Nice to have
• Bright colours.

```html
<!DOCTYPE html>
<html lang="en">
<head>
<meta charset="utf-8">
<title>Heat Stroke Banner – Meadowlark Pet Hospital</title>
<link href="https://fonts.googleapis.com/css2?family=Oswald:wght@600&family=Montserrat:wght@700&display=swap" rel="stylesheet">
<style>
  :root {
    --page: #ffffff;
    --ink: #1d1d1d;
    --brand-ink: #4a2a16;
    --yellow: #f2f01c;
    --lime: #c6f04a;
    --pink: #ff5db1;
    --pink-soft: #ffc0de;
    --teal: #12d6b4;
    --blue: #19b2f5;
    --green: #7cbd1a;
    --orange: #e0860d;
    --peach: #ffd98a;
    --dog-dark: #5a3418;
    --dog-tan: #c49563;
    --dog-cream: #e9d3ae;
  }
  html, body {
    margin: 0;
    width: 1200px;
    height: 1200px;
    overflow: hidden;
    background: var(--page);
  }
  .banner {
    position: absolute;
    left: 7px;
    top: 334px;
    width: 1185px;
    height: 283px;
    overflow: hidden;
    font-family: "Montserrat", Arial, sans-serif;
  }
  .banner-bg { position: absolute; inset: 0; }
  .title {
    position: absolute;
    left: 420px;
    top: 18px;
    width: 300px;
    margin: 0;
    text-align: center;
    font-family: "Oswald", "Arial Narrow", sans-serif;
    font-weight: 600;
    font-style: italic;
    font-size: 54px;
    line-height: 1;
    letter-spacing: 1px;
    color: #ffffff;
    text-shadow: 2px 3px 3px rgba(0,0,0,0.55);
  }
  .symptoms {
    position: absolute;
    z-index: 2;
    margin: 0;
    padding: 0;
    list-style: none;
    font-weight: 700;
    font-size: 10px;
    line-height: 12px;
    letter-spacing: 0.5px;
    text-transform: uppercase;
    white-space: nowrap;
    color: var(--ink);
  }
  .symptoms li::before { content: "- "; }
  .symptoms .cont { padding-left: 9px; }
  .symptoms .cont::before { content: ""; }
  .symptoms-early { left: 134px; top: 119px; }
  .symptoms-mid { left: 567px; top: 96px; }
  .symptoms-late { left: 963px; top: 212px; }
  .dog {
    position: absolute;
    z-index: 1;
    border: 3px solid #ffffff;
    box-sizing: border-box;
  }
  .dog-sitting {
    left: 35px; top: 42px; width: 90px; height: 206px;
    border-radius: 45% 45% 20% 20%;
    background: linear-gradient(180deg, var(--dog-dark), #2a170b);
  }
  .dog-lying {
    left: 385px; top: 90px; width: 176px; height: 174px;
    border-radius: 40% 40% 18% 30%;
    background: linear-gradient(160deg, var(--dog-tan), #a97845);
  }
  .dog-staggering {
    left: 933px; top: 106px; width: 140px; height: 94px;
    border-radius: 40%;
    background: linear-gradient(180deg, var(--dog-cream), #d8bb8d);
  }
  .brand {
    position: absolute;
    z-index: 2;
    left: 1063px;
    top: 10px;
    width: 112px;
    height: 90px;
    background: #ffffff;
    display: flex;
    align-items: center;
    justify-content: center;
    text-align: center;
    font-weight: 700;
    font-size: 13px;
    line-height: 16px;
    color: var(--brand-ink);
    text-transform: uppercase;
  }
</style>
</head>
<body>
<section class="banner">
  <svg class="banner-bg" viewBox="0 0 1185 283" width="1185" height="283" aria-hidden="true">
    <defs>
      <linearGradient id="panel-one" x1="0" x2="1">
        <stop offset="0" stop-color="#d0d0d0"/><stop offset="1" stop-color="#e6e6e6"/>
      </linearGradient>
      <linearGradient id="panel-two" x1="0" x2="1">
        <stop offset="0" stop-color="#c8c8c8"/><stop offset="1" stop-color="#a9a9a9"/>
      </linearGradient>
      <linearGradient id="panel-three" x1="0" x2="1">
        <stop offset="0" stop-color="#b5b5b5"/><stop offset="1" stop-color="#9a9a9a"/>
      </linearGradient>
      <linearGradient id="chevron-shade" x1="0" x2="1">
        <stop offset="0" stop-color="#f4f4f4"/><stop offset="1" stop-color="#2b2b2b"/>
      </linearGradient>
    </defs>
    <rect width="1185" height="283" fill="url(#panel-three)"/>
    <polygon points="0,0 840,0 893,141 840,283 0,283" fill="url(#panel-two)"/>
    <polygon points="0,0 270,0 330,141 258,283 0,283" fill="url(#panel-one)"/>

    <polygon points="0,130 70,60 20,283 0,283" fill="var(--yellow)"/>
    <polygon points="0,170 90,283 0,283" fill="var(--lime)"/>
    <polygon points="60,283 125,175 150,283" fill="var(--pink-soft)"/>
    <polygon points="0,230 40,150 80,283" fill="var(--peach)" opacity="0.7"/>
    <polygon points="140,60 188,80 150,108" fill="var(--pink)" opacity="0.55"/>
    <polygon points="35,0 70,0 70,8" fill="var(--yellow)"/>
    <polygon points="250,283 300,210 310,283" fill="var(--teal)"/>
    <circle cx="38" cy="29" r="8" fill="var(--peach)"/>
    <circle cx="159" cy="16" r="8" fill="var(--peach)"/>
    <circle cx="314" cy="176" r="7" fill="var(--peach)"/>

    <polygon points="358,283 366,265 372,283" fill="var(--lime)"/>

    <polygon points="1040,20 1185,20 1185,120 1150,160" fill="var(--teal)"/>
    <polygon points="990,120 1060,130 1130,283 1060,283" fill="var(--blue)"/>
    <polygon points="1080,170 1185,140 1185,283 1130,283" fill="var(--green)"/>
    <polygon points="1150,130 1185,100 1185,200" fill="var(--teal)"/>
    <polygon points="850,205 903,180 903,243" fill="var(--pink)"/>
    <polygon points="940,283 970,235 1040,283" fill="var(--pink)"/>
    <polygon points="818,250 840,283 920,283" fill="var(--yellow)" opacity="0.8"/>
    <polygon points="860,240 930,283 880,283" fill="var(--green)" opacity="0.7"/>
    <circle cx="1025" cy="77" r="8" fill="var(--orange)"/>
    <circle cx="1100" cy="108" r="8" fill="var(--orange)"/>
    <circle cx="926" cy="222" r="8" fill="var(--orange)"/>

    <polygon points="270,0 294,0 354,141 282,283 258,283 330,141" fill="#ffffff"/>
    <polygon points="294,0 318,0 381,141 306,283 282,283 354,141" fill="url(#chevron-shade)"/>
    <polygon points="769,0 793,0 853,141 783,283 759,283 829,141" fill="#ffffff"/>
    <polygon points="793,0 817,0 881,141 807,283 783,283 853,141" fill="url(#chevron-shade)"/>
  </svg>

  <h1 class="title">HEAT STROKE</h1>

  <div class="dog dog-sitting" role="img" aria-label="Photo of a panting Rottweiler sitting"></div>
  <ul class="symptoms symptoms-early">
    <li>Panting which increases</li>
    <li class="cont">as heatstroke progresses</li>
    <li>Drooling, salivating</li>
    <li>Agitation, restlessness</li>
    <li>Very red or pale gums</li>
    <li>Bright red tongue</li>
    <li>Increased heart rate</li>
  </ul>

  <div class="dog dog-lying" role="img" aria-label="Photo of a tan dog lying down with its head tilted"></div>
  <ul class="symptoms symptoms-mid">
    <li>Breathing distress</li>
    <li>Vomiting diarrhea</li>
    <li class="cont">(possibly with blood)</li>
    <li>Signs of mental confusion, delirium</li>
    <li>Dizziness, staggering</li>
    <li>Lethargy, weakness</li>
  </ul>

  <div class="dog dog-staggering" role="img" aria-label="Photo of a pale dog staggering and collapsing"></div>
  <ul class="symptoms symptoms-late">
    <li>Muscle tremors</li>
    <li>Seizures</li>
    <li>Collapsing and lying down</li>
    <li>Little to no urine production</li>
    <li>Coma</li>
  </ul>

  <div class="brand">Meadowlark<br>Pet<br>Hospital</div>
</section>
</body>
</html>
```